Flyer for IT Services

We need a flyer template for our different products and services we offer. We're an IT firm that provides Managed Services, Remote Backup, Mobile Device Management, Unified Communications, and more.

The flyer should be two sided and provide an area for an explanation of the service and then some pictures, lists of features, and a section for our contact info and company description.

We will normally send the flyer over to a client as a PDF via email but may also printer the flyers to hand out at meetings with prospects.

Information on the services to get ideas is at the following and the services heading:
www.fernridgetech.com

Target Market(s)

small to medium sized companies (2-150 employees)

Industry/Entity Type

Printer

Requirements
Must have
• Flyer must be two sided, include our logo, and have sections for product and company description as well as feature lists.

```html
<!DOCTYPE html>
<html lang="en">
<head>
<meta charset="utf-8">
<title>Managed Services Flyer – Front</title>
<link rel="stylesheet" href="https://fonts.googleapis.com/css2?family=Jost:wght@500;600;700&family=Montserrat:wght@700&family=Cinzel:wght@400&display=swap">
<style>
  :root {
    --page: #ffffff;
    --ink-light: #ffffff;
    --yellow-bright: #f6e600;
    --yellow-mid: #f7cf0a;
    --orange: #f4b40f;
    --label: #f5c400;
    --photo-green: #4d8a3c;
    --photo-pale: #dfe8ea;
    --photo-grey: #aab3b0;
    --photo-dark: #6c7872;
  }
  * { margin: 0; padding: 0; box-sizing: border-box; }
  html, body { width: 1200px; height: 900px; overflow: hidden; background: var(--page); }
  .canvas { position: relative; width: 1200px; height: 900px; }

  .flyer { position: absolute; left: 52px; top: 48px; width: 1095px; height: 707px; overflow: hidden; }
  .flyer-photo {
    position: absolute; left: 0; top: 0; width: 703px; height: 707px;
    background: linear-gradient(90deg, var(--photo-green) 0%, #7fa77a 7%, var(--photo-pale) 12%, #e9eeee 22%, var(--photo-grey) 45%, #8f9995 65%, var(--photo-dark) 85%, #52806a 100%);
  }
  .flyer-panel { position: absolute; left: 0; top: 0; }

  .tagline {
    position: absolute; left: 418px; top: 40px;
    font-family: "Cinzel", serif; font-size: 19px; line-height: 23px;
    color: var(--ink-light); letter-spacing: 0.5px;
  }

  .brand { position: absolute; right: 16px; top: 20px; display: flex; align-items: center; gap: 10px; }
  .brand-dot { width: 38px; height: 38px; border: 3px solid var(--ink-light); border-radius: 50%; }
  .brand-name { font-family: "Jost", sans-serif; font-weight: 700; font-size: 50px; line-height: 50px; color: var(--ink-light); letter-spacing: 2px; }
  .brand-url {
    position: absolute; right: 14px; top: 80px;
    font-family: "Jost", sans-serif; font-weight: 600; font-size: 16px; color: var(--ink-light);
  }

  .service-title {
    position: absolute; left: 625px; top: 285px;
    font-family: "Montserrat", sans-serif; font-weight: 700; font-size: 60px; line-height: 72px;
    color: var(--ink-light); letter-spacing: 1px;
  }

  .service-intro {
    position: absolute; left: 725px; top: 534px; width: 365px;
    font-family: "Jost", sans-serif; font-weight: 500; font-size: 15.5px; line-height: 22.6px;
    color: var(--ink-light);
  }

  .side-label {
    position: absolute; right: 55px; top: 795px;
    font-family: "Jost", sans-serif; font-weight: 500; font-size: 64px; line-height: 70px;
    color: var(--label);
  }
</style>
</head>
<body>
<div class="canvas">
  <section class="flyer">
    <div class="flyer-photo" role="img" aria-label="Photo of a smiling businesswoman on a phone call, jacket slung over her shoulder, in front of a bright office building"></div>

    <svg class="flyer-panel" width="1095" height="707" viewBox="0 0 1095 707" aria-hidden="true">
      <defs>
        <linearGradient id="panelFill" x1="0" y1="0" x2="1" y2="1">
          <stop offset="0" stop-color="var(--yellow-bright)"/>
          <stop offset="0.5" stop-color="var(--yellow-mid)"/>
          <stop offset="1" stop-color="var(--orange)"/>
        </linearGradient>
      </defs>
      <path d="M703 0 H1095 V707 H703 V507 A150 150 0 0 1 703 207 Z" fill="url(#panelFill)"/>
    </svg>

    <p class="tagline">Stop waiting for your<br>technology to break</p>

    <div class="brand">
      <span class="brand-dot"></span>
      <span class="brand-name">FRT</span>
    </div>
    <p class="brand-url">www.fernridgetech.com</p>

    <h1 class="service-title">MANAGED<br>SERVICES</h1>

    <p class="service-intro">Managed services from Fern Ridge Technology<br>provide you with more reliable performance<br>and more predictable expenses.<br>That means you get more value from the tech-<br>nology you've already invested in, while<br>actually reducing the total costs of IT problems<br>and the resulting downtime.</p>
  </section>

  <p class="side-label">FRONT</p>
</div>
</body>
</html>
```